Graphic design for "How It Works" for VelmoraStyles.com*

VelmoraStyles.com website is for selling custom designer outfits for women and girls in all countries, customers can choose existing designs on this website and customize to their measurements. Customers can also provide their own designs and measurements and our expert designers and tailors get the outfit stitched and delivered to the customer.

We wanted to explain how this entire process works in 4 steps in the form of graphic design with little heading and text describing each step.

Step 1: Select Dress
Its time to choose the beauty you want to adorn yourself with. We have a wide collection of premium dresses, colours and accessories. There is something for everyone! All you need to do is pick. If you can’t find what you are looking for then you can share a picture of what you want, we will get it done whatever you want.

Step 2: Customization
Everyone is different; hence we realise the need for customization of the design and size. Here you select exactly how you want your dress to be. From sleeves to cuts, everything will be done as per your wish. Enter your measurements, lo and behold! You’re done. Leave your comments for even more customization.

Step 3: Designer Consultation
We as a user-friendly brand, aspire to provide the best of services to our clients. Our expert lady designers will help you for everything right from selecting of fabric to design of dress to necessary accessories. Our designers are just a call away!

Step 4: Stitch and Deliver
After you have placed your order, we confirm and verify the details. The boutique completes your order, sends it to us and we deliver it to your doorstep. We also have a team of designers in-house to cater to your premium dressing needs.

```html
<!DOCTYPE html>
<html lang="en">
<head>
<meta charset="utf-8">
<title>How It Works – VelmoraStyles.com</title>
<link rel="stylesheet" href="https://fonts.googleapis.com/css2?family=Montserrat:wght@500;600;800&family=Oswald:wght@600&display=swap">
<style>
  :root {
    --brand-pink: #c75185;
    --step-pink: #c8467f;
    --pale-pink: #f6e4ee;
    --sketch-pink: #f0cfe0;
    --ink: #2a2438;
    --body-ink: #222;
    --frame-grey: #6b6b6b;
    --paper: #ffffff;
  }
  * { margin: 0; padding: 0; box-sizing: border-box; }
  html, body { width: 703px; height: 1200px; overflow: hidden; background: var(--paper); }
  .flyer { position: relative; width: 703px; height: 1200px; background: var(--paper); overflow: hidden; }

  .masthead {
    position: absolute; left: 0; top: 0; width: 100%; height: 110px;
    background: var(--brand-pink);
    display: flex; align-items: center; justify-content: center;
  }
  .masthead::after {
    content: ""; position: absolute; left: 0; right: 0; bottom: 2px;
    border-bottom: 2px dashed var(--paper);
  }
  .brand-name {
    font-family: "Montserrat", sans-serif; font-weight: 800;
    font-size: 50px; color: var(--ink); letter-spacing: -0.5px;
  }

  .side-sketch {
    position: absolute; top: 125px; width: 38px; height: 1020px;
    background: linear-gradient(180deg, var(--sketch-pink), #fbeef5 50%, var(--sketch-pink));
    opacity: 0.6;
  }
  .side-sketch.left { left: 0; }
  .side-sketch.right { right: 0; }

  .steps-frame {
    position: absolute; left: 36px; top: 143px; width: 631px; height: 997px;
    border: 2px dashed var(--frame-grey); border-radius: 44px;
    background: var(--paper);
  }

  .step-art {
    position: absolute; width: 190px; height: 190px; border-radius: 50%;
    border: 2px dashed #e07aa8;
    background: radial-gradient(circle, #f9eaf2 40%, var(--pale-pink));
  }

  .step-copy { position: absolute; }
  .step-number {
    font-family: "Oswald", sans-serif; font-weight: 600;
    font-size: 28px; color: var(--step-pink); line-height: 1.1;
  }
  .step-title {
    font-family: "Montserrat", sans-serif; font-weight: 800;
    font-size: 22px; color: var(--ink); margin: 6px 0 8px; letter-spacing: 0.3px;
  }
  .step-text {
    font-family: "Montserrat", sans-serif; font-weight: 600;
    font-size: 10.6px; line-height: 1.32; color: var(--body-ink);
    text-align: justify; hyphens: auto;
  }

  .site-url {
    position: absolute; left: 0; right: 0; top: 1160px; text-align: center;
    font-family: "Montserrat", sans-serif; font-weight: 500;
    font-size: 13px; letter-spacing: 3px; color: var(--ink);
  }
</style>
</head>
<body>
<main class="flyer">
  <header class="masthead">
    <span class="brand-name">velmorastyles</span>
  </header>

  <div class="side-sketch left" role="img" aria-label="Pink line sketches of dresses and sewing tools"></div>
  <div class="side-sketch right" role="img" aria-label="Pink line sketches of dresses, scissors and a sewing machine"></div>

  <section class="steps-frame" aria-label="How it works"></section>

  <div class="step-art" style="left:90px; top:197px;" role="img" aria-label="Illustration of a woman browsing red dresses on a large phone screen"></div>
  <article class="step-copy" style="left:329px; top:188px; width:262px;">
    <h2 class="step-number">STEP 01:</h2>
    <h3 class="step-title">SELECT DRESS</h3>
    <p class="step-text">Its time to choose the beauty you want to adorn yourself with. We have a wide collection of premium dresses, colours and accessories. There is something for everyone! All you need to do is pick. If you can’t find what you are looking for then you can share a picture of what you want, we will get it done whatever you want.</p>
  </article>

  <article class="step-copy" style="left:96px; top:452px; width:263px;">
    <h2 class="step-number">STEP 02:</h2>
    <h3 class="step-title">CUSTOMIZATION</h3>
    <p class="step-text">Everyone is different; hence we realise the need for customization of the design and size. Here you select exactly how you want your dress to be. From sleeves to cuts, everything will be done as per your wish. Enter your measurements, lo and behold! You’re done. Leave your comments for even more customization.</p>
  </article>
  <div class="step-art" style="left:409px; top:455px;" role="img" aria-label="Illustration of a laptop showing teal dress styles to choose from"></div>

  <div class="step-art" style="left:92px; top:686px;" role="img" aria-label="Illustration of a lady designer presenting dress sketches on an easel"></div>
  <article class="step-copy" style="left:335px; top:692px; width:320px;">
    <h2 class="step-number">STEP 03:</h2>
    <h3 class="step-title">DESIGNER CONSULTATION</h3>
    <p class="step-text" style="width:282px;">We as a user-friendly brand, aspire to provide the best of services to our clients. Our expert lady designers will help you for everything right from selecting of fabric to design of dress to necessary accessories. Our designers are just a call away!</p>
  </article>

  <article class="step-copy" style="left:98px; top:930px; width:285px;">
    <h2 class="step-number">STEP 04:</h2>
    <h3 class="step-title">STITCH AND DELIVER</h3>
    <p class="step-text">After you have placed your order, we confirm and verify the details. The boutique completes your order, sends it to us and we deliver it to your doorstep. We also have a team of designers in-house to cater to your premium dressing needs.</p>
  </article>
  <div class="step-art" style="left:411px; top:912px;" role="img" aria-label="Illustration of a tailor at a sewing machine and a courier handing a parcel to a customer"></div>

  <footer class="site-url">www.velmorastyles.com</footer>
</main>
</body>
</html>
```